Larkmoor Dental Center Specials/Offers

Take the advertisement pic (LABELED ADVERTISEMENT) and make it look "professional in appearance" using the logo and color scheme of Larkmoor Dental Center. The Phone number should be 614-382-2096. I want the same content, different background, professional looking document. I want it to be a 12"x12" document. High resolution files should include .PDF, .JPG and .AI. Any or all documents can be used for colors and overall scheme. I would like to have the overall colors include the main blue color from the file 4db749b4ef4c5e0717512bf7eb26bf54 and include the brown "swoosh" somewhere through/on the final document. Stock files of smiling young families can be used but not required. I am on a tight time-line and have placed 5 days as the deadline, but I will pick my favorite in as little as 2-3 days if I can get a good product. Again ALL the info from the Advertisement document should be included on the final product. Use any or all of the uploaded files for assistance. You can also visit our website for more info: www.larkmoordentalcenter.example Thanks

```html
<!DOCTYPE html>
<html lang="en">
<head>
<meta charset="utf-8">
<title>Larkmoor Dental Center – Specials</title>
<link href="https://fonts.googleapis.com/css2?family=Quicksand:wght@400;500&family=Roboto+Condensed:wght@400;700&family=Oswald:wght@500;600;700&family=Archivo+Black&family=Arimo:ital,wght@0,700;1,700&display=swap" rel="stylesheet">
<style>
  :root {
    --brown: #7a3a18;
    --brown-deep: #6b3114;
    --blue: #628d9c;
    --blue-text: #5a8a9c;
    --leaf: #dde6ea;
    --cream: #f4ede4;
    --white: #ffffff;
    --grey-text: #5d5a55;
    --panel: #d9e1e4;
  }
  * { margin: 0; padding: 0; box-sizing: border-box; }
  html, body { width: 1200px; height: 1200px; overflow: hidden; background: var(--white); }
  .ad { position: relative; width: 1200px; height: 1200px; background: var(--white); overflow: hidden; }
  .ad-frame {
    position: absolute; left: 47px; top: 47px; width: 1106px; height: 1106px;
    border: 2px solid var(--brown-deep);
    background: linear-gradient(180deg, #ffffff 0%, #faf6f1 30%, var(--cream) 60%);
  }
  .backdrop { position: absolute; left: 0; top: 0; width: 1200px; height: 1200px; }
  .abs { position: absolute; }

  .tree-art {
    left: 80px; top: 90px; width: 390px; height: 400px; border-radius: 48% 48% 30% 30%;
    background: radial-gradient(ellipse at 50% 40%, #9fbcc6 0%, #c7d7dc 45%, rgba(244,237,228,0) 72%),
                linear-gradient(180deg, rgba(122,58,24,0) 65%, rgba(122,58,24,0.3) 100%);
  }

  .brand-name {
    left: 497px; top: 78px; font-family: "Quicksand", sans-serif; font-weight: 500;
    font-size: 132px; line-height: 1; color: var(--brown); letter-spacing: -1px; white-space: nowrap;
  }
  .brand-sub {
    left: 497px; top: 216px; font-family: "Quicksand", sans-serif; font-weight: 400;
    font-size: 74px; line-height: 1; color: var(--grey-text); letter-spacing: 2px; white-space: nowrap;
  }
  .brand-services {
    left: 502px; top: 292px; font-family: "Quicksand", sans-serif; font-weight: 500;
    font-size: 37px; line-height: 1.2; color: var(--grey-text); letter-spacing: 2.5px; white-space: nowrap;
  }
  .brand-address {
    left: 500px; top: 350px; font-family: "Roboto Condensed", sans-serif; font-weight: 400;
    font-size: 28px; color: var(--grey-text); white-space: nowrap; word-spacing: 2px;
  }
  .brand-address span { margin-left: 36px; }

  .tagline {
    left: 530px; top: 480px; width: 620px; text-align: center; transform: rotate(-6deg);
    font-family: "Arimo", sans-serif; font-weight: 700; font-size: 25px; line-height: 1.2;
    color: var(--white); letter-spacing: 0.5px; white-space: nowrap;
  }

  .offer { text-align: center; font-family: "Oswald", sans-serif; line-height: 1.05; white-space: nowrap; }
  .offer-title { color: var(--brown); font-weight: 700; font-size: 48px; line-height: 1.1; letter-spacing: -0.5px; }
  .offer-title sup { font-size: 28px; vertical-align: 16px; }
  .offer-body { color: var(--blue-text); font-weight: 600; font-size: 28px; line-height: 1.1; }
  .offer-note { color: var(--brown); font-weight: 500; font-size: 18px; line-height: 1.15; margin-top: 2px; }

  .offer-new { left: 140px; top: 576px; width: 400px; transform: rotate(-5deg); }
  .offer-first { left: 770px; top: 556px; width: 340px; transform: rotate(-5deg); }
  .offer-first .offer-title { font-size: 60px; }
  .offer-bleach {
    left: 550px; top: 680px; width: 200px; transform: rotate(-10deg); color: var(--white);
    font-weight: 700; font-size: 36px; line-height: 1.05;
  }
  .offer-bleach .price { font-size: 56px; }
  .offer-bleach sup { font-size: 26px; vertical-align: 22px; }

  .providers {
    left: 47px; top: 880px; width: 1106px; text-align: center; font-family: "Arimo", sans-serif;
    font-weight: 700; font-size: 20px; line-height: 1.2; color: var(--white); letter-spacing: 1.5px;
  }
  .referral {
    left: 47px; top: 954px; width: 1106px; text-align: center; font-family: "Arimo", sans-serif;
    font-weight: 700; font-size: 19px; color: var(--white); letter-spacing: 1px;
  }
  .cta-panel {
    left: 160px; top: 1000px; width: 917px; height: 104px; background: var(--panel);
    display: flex; align-items: center; justify-content: space-between; padding: 0 10px 0 6px;
  }
  .cta-label {
    font-family: "Archivo Black", sans-serif; font-size: 37px; line-height: 0.98; color: var(--brown);
    letter-spacing: 2px; white-space: nowrap;
  }
  .cta-phone {
    font-family: "Oswald", sans-serif; font-weight: 600; font-size: 78px; line-height: 1;
    color: var(--brown); letter-spacing: 1px; white-space: nowrap;
  }
  .website {
    left: 47px; top: 1108px; width: 1106px; text-align: center; font-family: "Arimo", sans-serif;
    font-style: italic; font-weight: 700; font-size: 31px; color: var(--white); letter-spacing: 1px;
  }
</style>
</head>
<body>
<div class="ad">
  <div class="ad-frame"></div>

  <div class="abs tree-art" role="img" aria-label="Stylised tree with a brown trunk and blue-grey leaves"></div>

  <svg class="backdrop" viewBox="0 0 1200 1200" aria-hidden="true">
    <defs><clipPath id="frame-clip"><rect x="48" y="48" width="1104" height="1104"/></clipPath></defs>
    <g clip-path="url(#frame-clip)">
      <path class="blue-field" fill="#628d9c"
            d="M47 440 C250 540 500 552 700 540 C900 528 1050 506 1153 500 L1153 1153 L47 1153 Z"/>
      <path class="swoosh" fill="#7a3a18" stroke="#ffffff" stroke-width="4"
            d="M47 400 C200 470 400 500 700 484 C900 474 1050 436 1153 420 L1153 500 C1050 506 900 526 700 540 C500 552 250 540 47 440 Z"/>
      <path class="leaf leaf-left" fill="#dde6ea" stroke="#ffffff" stroke-width="12" stroke-linejoin="round"
            d="M87 660 C150 520 470 500 600 747 C470 840 170 830 87 660 Z"/>
      <path class="leaf leaf-right" fill="#dde6ea" stroke="#ffffff" stroke-width="12" stroke-linejoin="round"
            d="M713 687 C800 550 1060 510 1147 607 C1080 770 830 810 713 687 Z"/>
    </g>
  </svg>

  <div class="abs brand-name">Larkmoor</div>
  <div class="abs brand-sub">DENTAL CENTER</div>
  <div class="abs brand-services">FAMILY • COSMETIC • IMPLANTS</div>
  <div class="abs brand-address">2240 Fenwick Ave., Suite C<span>Alder Falls, OH 43210</span></div>

  <div class="abs tagline">WHERE THE WHOLE FAMILY CAN BE SEEN.</div>

  <div class="abs offer offer-new">
    <div class="offer-title"><sup>$</sup>59 NEW PATIENTS</div>
    <div class="offer-body">REGULAR CLEANING<br>&amp; COMPREHENSIVE EXAM<br>including&nbsp; X-RAYS</div>
    <div class="offer-note">ONLY PATIENTS WITHOUT<br>DENTAL BENEFITS</div>
  </div>

  <div class="abs offer offer-bleach">
    <div class="price"><sup>$</sup>99</div>
    <div>BLEACHING<br>SPECIAL</div>
  </div>

  <div class="abs offer offer-first">
    <div class="offer-title">20% OFF</div>
    <div class="offer-body">TREATMENT<br>SCHEDULED FIRST VISIT</div>
    <div class="offer-note">ONLY PATIENTS WITHOUT<br>DENTAL BENEFITS</div>
  </div>

  <div class="abs providers">PREFERRED PROVIDER FOR: HARBOR DENTAL, NORTHGATE LIFE, VELTRA,<br>CORVANE,&nbsp; SUMMIT SHIELD AND ALLIED MERIDIAN</div>
  <div class="abs referral">ASK ABOUT OUR REFERRAL PROGRAM.</div>

  <div class="abs cta-panel">
    <div class="cta-label">CALL TODAY FOR<br>AN APPOINTMENT:</div>
    <div class="cta-phone">614-382-2096</div>
  </div>

  <div class="abs website">www.larkmoordentalcenter.example</div>
</div>
</body>
</html>
```